Brantley Oakhollow LLC. custom built/handcrafted

I am recent small business owner looking to sell my art(drawings) and woodworking projects from my home. I have a very rough draft of a simple card design created on a simple digital program. I was hoping for a fancier lettering on the initial letters (BO). More of a calligraphy style. Also, the yellow border around the logo I would like to be a gold foil look. For it to be shiny or reflective look and to keep the other letters black with a consistent font on the card and the card white.

Target Market(s)

Local and neighboring cities

Industry/Entity Type

Art (drawing)/Woodworking

Contact Information for Business Card

My email rpoakhollow@mailbright.net, phone number 617-530-4168. In the files provided it has a yellow border around the logo and I was looking to make that a gold foil.

Font styles to use
Serif
Decorative
Script

Requirements
Nice to have
• symbols for having a Facebook and Instagram

```html
<!DOCTYPE html>
<html lang="en">
<head>
<meta charset="utf-8">
<title>Brantley Oakhollow LLC. — Business Card</title>
<link rel="stylesheet" href="https://fonts.googleapis.com/css2?family=Cinzel:wght@600;700&family=Montserrat:wght@500&display=swap">
<style>
  :root {
    --backdrop: #ece6dc;
    --wood-light: #a58d77;
    --wood-mid: #937a65;
    --wood-dark: #85705d;
    --gold: #d9a23e;
    --gold-deep: #b9842a;
    --card-shadow: rgba(40, 28, 15, 0.35);
  }
  * { box-sizing: border-box; margin: 0; padding: 0; }
  html, body { width: 1200px; height: 1200px; overflow: hidden; }
  body {
    background: var(--backdrop);
    font-family: "Cinzel", Georgia, serif;
    position: relative;
  }
  .card {
    position: absolute;
    left: 210px;
    width: 780px;
    height: 470px;
    background: linear-gradient(175deg, var(--wood-light) 0%, var(--wood-mid) 55%, var(--wood-dark) 100%);
    box-shadow: 0 10px 26px var(--card-shadow);
  }
  .card--front { top: 95px; }
  .card--back { top: 625px; }

  .gold-frame {
    position: absolute;
    border: 4px solid var(--gold);
  }
  .card--front .gold-frame { left: 38px; top: 36px; right: 38px; bottom: 44px; }
  .card--back .gold-frame { left: 140px; top: 30px; right: 100px; bottom: 92px; }

  .owner-name {
    position: absolute;
    top: 128px; left: 0; right: 0;
    text-align: center;
    font-size: 52px;
    font-weight: 700;
    color: var(--gold);
    letter-spacing: 1px;
  }
  .owner-title {
    position: absolute;
    top: 196px; left: 0; right: 0;
    text-align: center;
    font-size: 40px;
    font-weight: 700;
    color: var(--gold);
  }
  .contact {
    position: absolute;
    top: 280px;
    text-align: center;
    font-family: "Montserrat", Arial, sans-serif;
    font-size: 17px;
    font-weight: 500;
    color: var(--gold-deep);
  }
  .contact svg { display: block; margin: 0 auto 6px; }
  .contact--phone { left: 130px; width: 200px; top: 290px; }
  .contact--email { left: 430px; width: 300px; }
  .social {
    position: absolute;
    top: 372px; left: 0; right: 0;
    display: flex;
    justify-content: center;
    gap: 28px;
  }
  .social__mark {
    width: 34px; height: 34px;
    border: 3px solid var(--gold-deep);
  }
  .social__mark--round { border-radius: 50%; }
  .social__mark--square { border-radius: 7px; }

  .brand-name {
    position: absolute;
    left: 140px; right: 100px;
    top: 30px; bottom: 92px;
    display: flex;
    align-items: center;
    justify-content: center;
    font-size: 36px;
    font-weight: 700;
    color: var(--gold);
    letter-spacing: 1px;
  }
  .tagline {
    position: absolute;
    left: 0; right: 0;
    bottom: 22px;
    text-align: center;
    font-size: 36px;
    font-weight: 700;
    color: var(--gold);
    letter-spacing: 1px;
  }
</style>
</head>
<body>
  <section class="card card--front" aria-label="Card front">
    <div class="gold-frame"></div>
    <h1 class="owner-name">Russell P. Oakhollow</h1>
    <p class="owner-title">Owner</p>
    <div class="contact contact--phone">
      <svg width="52" height="38" viewBox="0 0 52 38" aria-hidden="true">
        <path d="M4 12 Q26 0 48 12 L44 18 L36 15 L35 10 Q26 7 17 10 L16 15 L8 18 Z" fill="var(--gold-deep)"/>
        <path d="M14 20 L38 20 L44 35 L8 35 Z" fill="var(--gold-deep)"/>
        <circle cx="26" cy="27" r="5" fill="var(--wood-mid)"/>
      </svg>
      617-530-4168
    </div>
    <div class="contact contact--email">
      <svg width="56" height="40" viewBox="0 0 56 40" aria-hidden="true">
        <rect x="3" y="3" width="50" height="34" fill="none" stroke="var(--gold-deep)" stroke-width="3"/>
        <path d="M3 3 L28 24 L53 3 M3 37 L22 19 M53 37 L34 19" fill="none" stroke="var(--gold-deep)" stroke-width="3"/>
      </svg>
      rpoakhollow@mailbright.net
    </div>
    <div class="social" aria-label="Social profiles">
      <span class="social__mark social__mark--round"></span>
      <span class="social__mark social__mark--square"></span>
    </div>
  </section>

  <section class="card card--back" aria-label="Card back">
    <div class="gold-frame"></div>
    <p class="brand-name">Brantley Oakhollow</p>
    <p class="tagline">Custom Build • Handcrafted</p>
  </section>
</body>
</html>
```